UPDATE: Web Page: Keystone Public Relations

i DON'T NEED PICTURES, JUST SOMETHING CLEAN LIKE THE ARTWORK ATTACHED OR BUILT ON BUSINESS CARDS...PLEASE DESIGN AROUND THAT.

I need a clean webpage for new public relations firm that I will launch on March 1st. I HAVE JUST ADDED BUSINESS CARD MODELS FOR WEB PAGE COVER AND START IN TERMS OF DESIGN.

Pull down categories: (built on this model: http://www.wendelmorrowpr.com/contact/)

-Home
-Services
-Expertise
-About Us
-Press
-Contact

Marcus Telfer, CEO
Keystone Public Relations
2875 West Maple Ave.
Los Angeles CA 90012
(o) 213.555.0142
(f) 213.555.0187
marcus@keystonekpr.com

Target Market(s)

Pacifica Assembly House, Halvern Civic Hall
Lobbying type services to government/public affairs

Industry/Entity Type

Business

Number of Pages Required

4 page

Requirements
Must have
• Portray a beautiful picture of LA City or a government hall way (not domes)
• 1. Public Relations---Pic of Advocacy
• 2. Public Affairs--pick of government capitol Sacramento/Halvern Civic Hall
• 3. Strategy & Advisory Services--Something smart like chalk board.
Nice to have
• Great Pics on slider pages
Should not have
• Assembly House Dome (California)
• Halvern Civic Hall

```html
<!DOCTYPE html>
<html lang="en">
<head>
<meta charset="utf-8">
<title>Keystone Public Relations</title>
<link rel="stylesheet" href="https://fonts.googleapis.com/css2?family=Titillium+Web:wght@300;400;600;700&family=PT+Serif:ital@1&display=swap">
<style>
:root{
  --blue:#1594d3;
  --black:#000;
  --ink:#fff;
  --grey-text:#b8b8b8;
  --panel-dark:#2c2c2c;
  --field:#2e2e2e;
}
*{margin:0;padding:0;box-sizing:border-box}
html,body{width:821px;height:1200px;overflow:hidden;background:var(--black)}
body{position:relative;font-family:"Titillium Web",Arial,sans-serif;color:var(--ink)}
.abs{position:absolute}

/* header */
.site-header{left:0;top:0;width:821px;height:100px;background:var(--black)}
.brand{left:64px;top:10px;display:flex;align-items:center;gap:8px}
.brand-mark{width:78px;height:78px;border-radius:50%;border:5px solid var(--blue)}
.brand-name{font-size:22px;font-weight:600;color:var(--blue);line-height:1.1;width:160px}
.main-nav{right:59px;top:41px;display:flex;font-size:10.5px;color:#d0d0d0}
.main-nav a{color:inherit;text-decoration:none}
.main-nav a.active{color:var(--blue)}
.main-nav .sep{margin:0 9px;color:#aaa}

/* hero */
.hero-photo{left:0;top:100px;width:646px;height:361px;
  background:
    radial-gradient(ellipse 180px 120px at 90px 300px,rgba(255,170,70,.45),rgba(255,170,70,0) 70%),
    radial-gradient(ellipse 260px 110px at 380px 190px,rgba(255,150,60,.35),rgba(255,150,60,0) 70%),
    radial-gradient(ellipse 420px 90px at 330px 40px,rgba(240,150,70,.55),rgba(240,150,70,0) 75%),
    linear-gradient(180deg,#a9551d 0%,#c8702a 22%,#7a4420 42%,#3a2416 60%,#22170f 80%,#150f0a 100%)}
.slider-arrows{left:593px;top:109px}
.contact-card{left:646px;top:100px;width:175px;height:180px;background:var(--black);padding:30px 0 0 26px;font-size:8px;font-weight:600;line-height:1.6}
.contact-card .title{text-align:center;width:118px;font-weight:700}
.contact-card .rule{width:9px;height:1px;background:#fff;margin:6px 0 8px 55px}
.contact-card .city{margin-top:9px;font-weight:700;font-size:8.5px}

/* service tiles */
.tile{text-align:center;font-size:9.3px;line-height:1.42}
.tile h3{font-size:10px;font-weight:600;text-transform:uppercase;line-height:1.3}
.tile .underline{width:52px;height:1px;margin:6px auto 10px}
.tile-dark{background:var(--black);color:var(--grey-text)}
.tile-dark h3{color:var(--blue)}
.tile-dark .underline{background:var(--blue)}
.tile-blue{background:var(--blue);color:#fff}
.tile-blue .underline{background:#fff;width:75px}
.services-band{left:252px;top:280px;width:394px;height:181px;background:var(--black)}
.svc-pr{left:276px;top:331px;width:152px}
.svc-mk{left:472px;top:331px;width:152px}
.svc-social{left:646px;top:280px;width:175px;height:181px;padding:30px 34px 0}

.industry{left:0;top:461px;width:252px;height:180px;padding-top:48px}
.industry ul{list-style:none;color:#cfcfcf}
.industry li::before{content:"• "}
.press{left:252px;top:461px;width:177px;height:180px;padding-top:48px}

/* founder */
.founder{left:429px;top:461px;width:392px;height:180px;
  background:
    radial-gradient(ellipse 110px 130px at 300px 80px,rgba(120,110,100,.45),rgba(120,110,100,0) 75%),
    linear-gradient(90deg,#ececec 0%,#e0e0e0 35%,#c4c6c8 62%,#a3a7ab 100%)}
.founder-copy{left:450px;top:505px;width:155px;color:#111;text-align:center}
.founder-copy h3{font-size:12.5px;font-weight:600;letter-spacing:.2px}
.founder-copy .name{color:var(--blue);font-size:10px;margin:8px 0 9px}
.founder-copy blockquote{font-family:"PT Serif",Georgia,serif;font-style:italic;font-size:10px;line-height:1.25;width:122px;margin:0 auto}
.quote-mark{font-family:Georgia,serif;font-size:22px;font-weight:700;color:#111;line-height:1}
.caption{left:675px;top:618px;font-family:"PT Serif",Georgia,serif;font-style:italic;font-size:10px;color:#111}

/* welcome */
.welcome{left:0;top:641px;width:821px;height:178px;background:var(--panel-dark);text-align:center;padding-top:26px}
.welcome h1{font-weight:300;font-size:23px;color:var(--blue);line-height:1.2}
.welcome .underline{width:75px;height:1px;background:var(--blue);margin:8px auto 10px}
.welcome p{width:560px;margin:0 auto;font-size:10.3px;line-height:1.4;color:#b5b5b5}

/* map */
.map{left:0;top:819px;width:821px;height:191px;
  background:
    radial-gradient(ellipse 170px 90px at 290px 70px,#c2c2c2,rgba(194,194,194,0) 75%),
    radial-gradient(ellipse 120px 80px at 470px 40px,#e4e4e4,rgba(228,228,228,0) 75%),
    linear-gradient(90deg,#d6d6d6 0%,#cfcfcf 20%,#dadada 45%,#d2d2d2 70%,#c8c8c8 84%,#d8d8d8 100%)}
.map-pin{left:403px;top:880px}
.map-rule{left:53px;top:1008px;width:401px;height:3px;background:var(--blue)}

/* footer */
.footer-info{left:130px;top:1040px;width:250px;text-align:center;font-size:9.3px;font-weight:600;color:#d4d4d4;line-height:1.35}
.footer-info h2,.quick-contact h2{font-size:18px;font-weight:400;color:var(--blue)}
.footer-info .rule{width:13px;height:1px;background:#888;margin:10px auto 10px}
.footer-info p{margin-bottom:12px}
.quick-contact{left:502px;top:1040px;width:228px}
.quick-contact h2{text-align:center;padding-right:14px;margin-bottom:12px}
.field-row{display:flex;align-items:flex-start;font-size:9px;font-weight:600;color:#d4d4d4;margin-bottom:7px}
.field-row label{width:49px;padding-top:2px}
.field{background:var(--field);border:0}
.field-email{width:178px;height:19px}
.field-msg{width:178px;height:43px}
.submit{margin-left:182px;width:46px;height:19px;background:var(--blue);color:#fff;font-family:inherit;font-size:9px;font-weight:600;border:0}
</style>
</head>
<body>

<header class="site-header abs">
  <div class="brand abs">
    <span class="brand-mark"></span>
    <span class="brand-name">Keystone Public Relations</span>
  </div>
  <nav class="main-nav abs">
    <a class="active" href="#">Home</a><span class="sep">|</span>
    <a href="#">Services</a><span class="sep">|</span>
    <a href="#">Expertise</a><span class="sep">|</span>
    <a href="#">About Us</a><span class="sep">|</span>
    <a href="#">Press</a><span class="sep">|</span>
    <a href="#">Contact Us</a>
  </nav>
</header>

<div class="hero-photo abs" role="img" aria-label="Los Angeles downtown skyline at dusk with city lights"></div>
<svg class="slider-arrows abs" width="38" height="20" viewBox="0 0 38 20" aria-hidden="true">
  <polyline points="8,2 2,10 8,18" fill="none" stroke="#fff" stroke-width="1.4"/>
  <polyline points="30,2 36,10 30,18" fill="none" stroke="#fff" stroke-width="1.4"/>
</svg>

<aside class="contact-card abs">
  <div class="title">KEYSTONE<br>PUBLIC RELATIONS</div>
  <div class="rule"></div>
  <div>(o) 213.555.0142</div>
  <div>(f) 213.555.0187</div>
  <div style="margin-top:8px;font-weight:400">marcus@keystonekpr.com</div>
  <div class="city">LOS ANGELES</div>
</aside>

<div class="services-band abs"></div>
<section class="tile tile-dark svc-pr abs">
  <h3>Public Relation</h3><div class="underline"></div>
  <p>Sed ut perspiciatis unde omnis iste natus error sit voluptatem accusantium doloremque laudantium, totam rem aperiam, eaque ipsa quae ab illo inventore</p>
</section>
<section class="tile tile-dark svc-mk abs">
  <h3>Marketing</h3><div class="underline"></div>
  <p>Sed ut perspiciatis unde omnis iste natus error sit voluptatem accusantium doloremque laudantium, totam rem aperiam,</p>
</section>
<section class="tile tile-blue svc-social abs">
  <h3>Social Media<br>Marketing</h3><div class="underline"></div>
  <p>Sed ut perspiciatis unde omnis iste natus errsitvoluptatemaccusa ntium doloremque laudantium, totam rem aperiam, eaque ipsa</p>
</section>

<section class="tile tile-dark industry abs">
  <h3>Industry We Love</h3><div class="underline"></div>
  <ul>
    <li>Public Relations</li>
    <li>Public Affairs</li>
    <li>Strategy &amp; Advisory Services</li>
  </ul>
</section>
<section class="tile tile-blue press abs">
  <h3>Recent Press</h3>
  <p style="margin:12px 0 12px">05.06</p>
  <p>The Harbor Ledger<br>Tough Love Isn't Easy to Give...</p>
</section>

<div class="founder abs" role="img" aria-label="Portrait photo of the founder in an office"></div>
<span class="quote-mark abs" style="left:441px;top:497px">&ldquo;</span>
<div class="founder-copy abs">
  <h3>MEET THE FOUNDER</h3>
  <p class="name">Marcus Telfer, CEO</p>
  <blockquote>Sed ut perspiciatis omnis iste natus error sit rem aperiam, eaque ipsa quae ab illo inventore veritatis</blockquote>
</div>
<span class="quote-mark abs" style="left:556px;top:614px">&rdquo;</span>
<span class="caption abs">Marcus Telfer, CEO</span>

<section class="welcome abs">
  <h1>Welcome to Keystone Public Relations</h1>
  <div class="underline"></div>
  <p>Lorem ipsum dolor sit amet, consectetur adipiscing elit. Donec bibendum blandit ipsum, in gravida velit efficitur id. Vivamus eget purus nibh. Maecenas ut arcu ut leo elementum vehicula at id orci. In hac habitasse platea dictumst. Pellentesque habitant morbi tristique senectus et netus et malesuada fames ac turpis egestas. Maecenas mollis ligula eget congue sodales. Etiam fermentum, purus ut gravida finibus, lectus ex dictum eros, non aliquet erat dolor vel dolor. Curabitur in eros sed quam volutpat fringilla et ac risus. Suspendisse eget eros eros.</p>
</section>

<div class="map abs" role="img" aria-label="Street map of the office location in Los Angeles"></div>
<svg class="map-pin abs" width="14" height="22" viewBox="0 0 14 22" aria-hidden="true">
  <path d="M7 1C3.7 1 1 3.6 1 6.9 1 11.5 7 21 7 21s6-9.5 6-14.1C13 3.6 10.3 1 7 1z" fill="#6e6e6e" stroke="#4a4a4a" stroke-width="1"/>
  <circle cx="7" cy="7" r="2.2" fill="#d8d8d8"/>
</svg>
<div class="map-rule abs"></div>

<footer>
  <div class="footer-info abs">
    <h2>Keystone Public Relations</h2>
    <div class="rule"></div>
    <p>2875 West Maple Ave.<br>Los Angeles CA 90012</p>
    <p>(o) 213.555.0142<br>(f) 213.555.0187</p>
    <p>(e) marcus@keystonekpr.com</p>
  </div>
  <form class="quick-contact abs">
    <h2>Quick Contact</h2>
    <div class="field-row"><label>Email:</label><span class="field field-email"></span></div>
    <div class="field-row"><label>Message:</label><span class="field field-msg"></span></div>
    <button class="submit" type="button">Submit</button>
  </form>
</footer>

</body>
</html>
```